GPS Tracker Business Card Design

We need a business card for a GPS Vehicle tracking company. We sell the hardware for the vehicle and the software platform to monitor your vehicle/s. Including high asset non-powered vehicles like a trailer using our solar powered unit.
We like using dark blue to different shades of blue along with gold. We have phone apps for Android and Apple devices.

We have a platform for families wanting to track their teenage driver and children; Plus a Fleet vehicle tracking platform.

Features: unlimited number of vehicles and/or assets including snow mobiles forklifts generators trailers airport equipment

Reports for driving behavior reports and alerts dashboard fleet maintenace timeline view and replay geofence real time alerts logbook scheduling route optimization accounting integration fleet grouping closest vehicle locator On Board Diagnostics.

Benefits: Increased productivity improved fuel efficiency organizing your business improve time management simplify back end processes, reduce fleet fuel efficiency and expenses increase fleet security etc..

Please view website: Velmorix.com

Industry/Entity Type

Business

Contact Information for Business Card

Harold P Simkins

```html
<!DOCTYPE html>
<html lang="en">
<head>
<meta charset="utf-8">
<title>Velmorix Business Card</title>
<link rel="stylesheet" href="https://fonts.googleapis.com/css2?family=Arimo:wght@400;700&display=swap">
<style>
  :root {
    --backdrop: #3b3430;
    --card: #1c1c1e;
    --card-edge: #262628;
    --ink-white: #f2f2f2;
    --ink-grey: #8a8a8e;
    --ink-silver: #a9a9ad;
    --ink-dim: #5d5d61;
    --brand-blue: #1a5fc8;
    --rule: #6e6e72;
  }
  * { box-sizing: border-box; margin: 0; padding: 0; }
  html, body {
    width: 1200px; height: 787px; overflow: hidden;
    background: var(--backdrop);
  }
  .stage {
    width: 1200px; height: 787px;
    display: flex; align-items: center; justify-content: center; gap: 44px;
  }
  .card {
    position: relative;
    width: 530px; height: 303px;
    background: var(--card);
    border: 1px solid var(--card-edge);
    box-shadow: 0 10px 30px rgba(0,0,0,.45);
    font-family: "Arimo", sans-serif;
  }
  .brand { line-height: 1; }
  .brand-name { font-weight: 400; }
  .brand-tagline { font-weight: 400; color: var(--ink-grey); letter-spacing: .5px; }

  /* front */
  .card-front .brand {
    position: absolute; left: 50%; top: 50%;
    transform: translate(-50%, -50%);
    text-align: center;
  }
  .card-front .brand-name { font-size: 58px; color: var(--ink-silver); }
  .card-front .brand-tagline { font-size: 17px; margin-top: 10px; color: var(--ink-dim); }

  /* back */
  .card-back .brand { position: absolute; right: 44px; top: 50px; text-align: right; }
  .card-back .brand-name { font-size: 54px; color: var(--ink-white); }
  .card-back .brand-tagline { font-size: 15px; margin-top: 8px; }

  .contact {
    position: absolute; left: 40px; top: 172px;
    display: flex; align-items: stretch;
  }
  .person { text-align: right; padding-right: 22px; }
  .person-name { color: var(--brand-blue); font-size: 19px; font-weight: 700; }
  .person-title { color: var(--ink-grey); font-size: 15px; margin: 2px 0 10px; }
  .person-address { color: var(--ink-white); font-size: 14px; line-height: 1.35; }
  .divider { width: 1px; background: var(--rule); margin: 6px 0; }
  .channels { list-style: none; padding-left: 22px; }
  .channels li {
    display: flex; align-items: center; gap: 10px;
    color: var(--ink-white); font-size: 15px; line-height: 25px;
  }
  .channels svg { width: 15px; height: 15px; fill: var(--brand-blue); flex: none; }
</style>
</head>
<body>
<main class="stage">
  <section class="card card-front" aria-label="Card front">
    <div class="brand">
      <div class="brand-name">Velmorix</div>
      <div class="brand-tagline">Every Mile, Every Asset</div>
    </div>
  </section>

  <section class="card card-back" aria-label="Card back">
    <div class="brand">
      <div class="brand-name">Velmorix</div>
      <div class="brand-tagline">Every Mile, Every Asset</div>
    </div>

    <div class="contact">
      <div class="person">
        <div class="person-name">Harold P Simkins</div>
        <div class="person-title">President</div>
        <div class="person-address">4127 Harwood Lane<br>Elm Ridge, NY 11702</div>
      </div>
      <div class="divider"></div>
      <ul class="channels">
        <li>
          <svg viewBox="0 0 16 16" aria-hidden="true"><path d="M2 4c0-1.5 2.5-2.5 6-2.5S14 2.5 14 4v1.5h-3V4.2H5v1.3H2zM4 7h8l2 6.5H2z"/></svg>
          866-410-2785
        </li>
        <li>
          <svg viewBox="0 0 16 16" aria-hidden="true"><path d="M4 1h8v4H4zM1 6h14v6h-3v3H4v-3H1zm4 4v4h6v-4z"/></svg>
          856 3197 4402
        </li>
        <li>
          <svg viewBox="0 0 16 16" aria-hidden="true"><path d="M1 3h14v1.2L8 9 1 4.2zM1 5.8l7 4.8 7-4.8V13H1z"/></svg>
          harold@velmorix.com
        </li>
        <li>
          <svg viewBox="0 0 16 16" aria-hidden="true"><circle cx="8" cy="8" r="7"/><path d="M1 8h14M8 1c-3 3.5-3 10.5 0 14M8 1c3 3.5 3 10.5 0 14" stroke="#1c1c1e" stroke-width="1" fill="none"/></svg>
          www.velmorix.com
        </li>
      </ul>
    </div>
  </section>
</main>
</body>
</html>
```